I need a business card designed using the logo provided either vertical or horizontal......Crestmoor Property Partners is an Australian based real estate company that caters for the upper end of the market so the design of the business card "must reflect" the companies image!!
Colour combinations are optional but "must be realistic" and must be able to be accurately useable CMYK colours.
Please consider that any colours used "must be able to be used" and be suitable in following designs for "pull out banner signs" and "real estate signs".
The colours and the font in the attached designs are for example and other combinations are encouraged.
Target Market(s)
The High End of the Australian real estate market
Industry/Entity Type
Business
Contact Information for Business Card
Logo - Business Name - Director + Licensed Real Estate Agent - Mobile Number (Cell Phone) - Business Number - Fax - Email Address - Web address
Requirements
Must have
- Designs and colours (CMYK) that can easily be interpreted by an Australian printer.
Nice to have
- Some alternative ideas on colour and font..........the ones provided are ok and have been provided as an example but I am looking for alternative ideas
Should not have
- Loud, overly bright colours. Designs that do not reflect the professional standards of the business.
- Designs that look good on a computer monitor but can not be re-created on a printing press.............this is most important when it comes to shading etc.

```html
<!DOCTYPE html>
<html lang="en">
<head>
<meta charset="utf-8">
<title>Crestmoor Property Partners – Business Card</title>
<link href="https://fonts.googleapis.com/css2?family=Open+Sans:wght@400;600;700&display=swap" rel="stylesheet">
<style>
  :root {
    --backdrop: #d9d9d9;
    --card-white: #ffffff;
    --card-black: #0c0c0c;
    --gold: #c8912f;
    --gold-light: #e2c48a;
    --gold-dark: #a26d1c;
    --ink: #222222;
    --text-light: #e8e2d6;
  }
  * { margin: 0; padding: 0; box-sizing: border-box; }
  html, body {
    width: 1200px; height: 852px; overflow: hidden;
    background: var(--backdrop);
    font-family: "Open Sans", Arial, sans-serif;
  }
  .card {
    position: absolute;
    width: 520px; height: 300px;
    border-radius: 22px;
    overflow: hidden;
    background: var(--card-white);
    box-shadow: 0 6px 16px rgba(0,0,0,0.18);
  }
  .card-front { left: 100px; top: 110px; }
  .card-back  { left: 580px; top: 440px; }

  .brand {
    position: absolute;
    display: flex; align-items: center; gap: 12px;
    color: var(--ink);
    font-weight: 600;
    text-transform: uppercase;
    letter-spacing: 0.06em;
    line-height: 1.15;
  }
  .brand-dot {
    width: 16px; height: 16px; border-radius: 50%;
    background: var(--gold); flex: none;
  }
  .card-front .brand { left: 130px; top: 118px; font-size: 24px; width: 320px; }
  .card-back .brand { left: 38px; top: 110px; font-size: 19px; width: 230px; }

  .back-panel { position: absolute; inset: 0; }

  .contact {
    position: absolute; left: 322px; top: 48px;
    color: var(--text-light);
    font-size: 11.5px;
  }
  .contact-name { color: var(--gold); font-weight: 700; font-size: 15px; }
  .contact-role { font-size: 10px; margin: 4px 0 0 18px; }
  .contact-list { list-style: none; margin-top: 30px; }
  .contact-list li { display: flex; align-items: center; gap: 8px; height: 17px; }
  .contact-list svg { width: 11px; height: 11px; flex: none; }
  .highlight { color: var(--gold); }
  .contact-address { margin: 8px 0 0 19px; line-height: 1.4; }
</style>
</head>
<body>

<section class="card card-front" aria-label="Business card front">
  <div class="brand"><span class="brand-dot"></span><span>Crestmoor Property Partners</span></div>
</section>

<section class="card card-back" aria-label="Business card back">
  <svg class="back-panel" viewBox="0 0 520 300" width="520" height="300" aria-hidden="true">
    <defs>
      <linearGradient id="gold-sweep" x1="0" y1="0" x2="0" y2="1">
        <stop offset="0" stop-color="#a26d1c"/>
        <stop offset="0.5" stop-color="#e2c48a"/>
        <stop offset="1" stop-color="#c8912f"/>
      </linearGradient>
    </defs>
    <path d="M205 0 H520 V300 H292 C336 200 318 82 205 0 Z" fill="var(--card-black)"/>
    <path d="M190 0 C304 78 326 196 278 300" fill="none" stroke="url(#gold-sweep)" stroke-width="6"/>
  </svg>

  <div class="brand"><span class="brand-dot"></span><span>Crestmoor Property Partners</span></div>

  <div class="contact">
    <div class="contact-name">Your Long Name</div>
    <div class="contact-role">Managing Director</div>
    <ul class="contact-list">
      <li>
        <svg viewBox="0 0 12 12" aria-hidden="true"><path d="M2 1h3l1 3-1.5 1a6 6 0 0 0 2.5 2.5L8 6l3 1v3a1 1 0 0 1-1 1A9 9 0 0 1 1 2a1 1 0 0 1 1-1z" fill="var(--gold)"/></svg>
        <span>00.00.00.0000</span>
      </li>
      <li>
        <svg viewBox="0 0 12 12" aria-hidden="true"><rect x="3" y="0.5" width="6" height="11" rx="1.2" fill="var(--gold)"/><rect x="4" y="2" width="4" height="7" fill="var(--card-black)"/></svg>
        <span>00.00.00.0000</span>
      </li>
      <li>
        <svg viewBox="0 0 12 12" aria-hidden="true"><rect x="0.5" y="2.5" width="11" height="7" fill="var(--gold)"/><path d="M0.5 2.5 6 7l5.5-4.5" fill="none" stroke="var(--card-black)" stroke-width="1"/></svg>
        <span>yourname@yourwebsite.com</span>
      </li>
      <li>
        <svg viewBox="0 0 12 12" aria-hidden="true"><circle cx="6" cy="6" r="5" fill="var(--gold)"/><path d="M1 6h10M6 1c-2.5 3-2.5 7 0 10M6 1c2.5 3 2.5 7 0 10" fill="none" stroke="var(--card-black)" stroke-width="0.8"/></svg>
        <span>www.<span class="highlight">yourwebsite</span>.com</span>
      </li>
    </ul>
    <p class="contact-address">Your Commercial or office address<br>in just two line with pincode</p>
  </div>
</section>

</body>
</html>
```